Business Management Fortress

Assist with enhancing a powerpoint slide by providing a few design options for consideration. I have a template but open to any creative ideas.

Target Market(s)

Internal employees and stakeholders

Industry/Entity Type

Business Management, Finance, Accounting

Requirements
Must have
• Maintain a fortress, temple, or pyramid schema
Nice to have
• Scenic Background

```html
<!DOCTYPE html>
<html lang="en">
<head>
<meta charset="utf-8">
<title>Business Management Fortress</title>
<link href="https://fonts.googleapis.com/css2?family=Open+Sans:wght@400;700&display=swap" rel="stylesheet">
<style>
  :root {
    --jungle-deep: #0f1c14;
    --jungle-mid: #2c4a2c;
    --jungle-light: #5f8a54;
    --sky: #9fd0e6;
    --apex-red: #e84a3c;
    --apex-red-side: #d2392f;
    --band-orange: #d97028;
    --band-orange-side: #c9621f;
    --peak-peach: #fbbf86;
    --peak-peach-side: #efa972;
    --ledge-green: #7a9a3e;
    --ledge-green-side: #6a8a34;
    --tier-green: #bcd591;
    --tier-green-side: #a8c07e;
    --ledge-teal: #3b8a78;
    --ledge-teal-side: #347d6c;
    --tier-mint: #a0d4c8;
    --tier-mint-side: #8ebfb2;
    --ledge-blue: #0e7a8e;
    --ledge-blue-side: #0b6c7e;
    --tier-blue: #68cbe2;
    --tier-blue-side: #58b6cf;
    --base-dark: #1f3840;
    --label: #ffffff;
  }
  html, body { margin: 0; padding: 0; overflow: hidden; background: #000; }
  .slide {
    position: relative;
    width: 1200px;
    height: 675px;
    overflow: hidden;
    font-family: "Open Sans", sans-serif;
  }
  .scenery {
    position: absolute;
    inset: 0;
    background:
      radial-gradient(ellipse 22% 45% at 50% 10%, var(--sky) 0%, rgba(159,208,230,0.5) 45%, rgba(159,208,230,0) 100%),
      radial-gradient(ellipse 45% 70% at 50% 40%, var(--jungle-light) 0%, var(--jungle-mid) 55%, var(--jungle-deep) 100%);
  }
  .pyramid {
    position: absolute;
    inset: 0;
    width: 1200px;
    height: 675px;
  }
  .tier-label {
    font-family: "Open Sans", sans-serif;
    font-weight: 700;
    fill: var(--label);
    text-anchor: middle;
  }
  .tier-label--lead { font-size: 34px; }
  .tier-label--main { font-size: 31px; }
  .tier-caption {
    font-family: "Open Sans", sans-serif;
    font-weight: 400;
    font-size: 27px;
    fill: var(--label);
    text-anchor: middle;
  }
  .slide-number {
    position: absolute;
    right: 22px;
    bottom: 14px;
    font-family: "Open Sans", sans-serif;
    font-size: 8px;
    color: #ffffff;
  }
</style>
</head>
<body>
<div class="slide">
  <div class="scenery" role="img" aria-label="Scenic background: ancient stone temple ruins in a lush jungle, trees framing a bright blue sky"></div>

  <svg class="pyramid" viewBox="0 0 1920 1080" aria-label="Business management pyramid">
    <!-- base plinth -->
    <polygon fill="var(--base-dark)" points="212,995 1710,995 1840,1080 80,1080"/>

    <!-- fiduciary tier -->
    <polygon fill="var(--ledge-blue-side)" points="392,771 1522,771 1605,818 312,818"/>
    <polygon fill="var(--ledge-blue)" points="678,771 1232,771 1255,818 655,818"/>
    <polygon fill="var(--tier-blue-side)" points="312,818 1605,818 1710,995 212,995"/>
    <polygon fill="var(--tier-blue)" points="655,818 1255,818 1322,995 588,995"/>

    <!-- capability tier -->
    <polygon fill="var(--ledge-teal-side)" points="575,550 1338,550 1420,597 493,597"/>
    <polygon fill="var(--ledge-teal)" points="770,550 1143,550 1162,597 745,597"/>
    <polygon fill="var(--tier-mint-side)" points="493,597 1420,597 1522,771 392,771"/>
    <polygon fill="var(--tier-mint)" points="745,597 1162,597 1232,771 678,771"/>

    <!-- profitability tier -->
    <polygon fill="var(--ledge-green-side)" points="817,328 1097,328 1237,372 677,372"/>
    <polygon fill="var(--ledge-green)" points="855,328 1052,328 1072,372 838,372"/>
    <polygon fill="var(--tier-green-side)" points="677,372 1237,372 1338,550 575,550"/>
    <polygon fill="var(--tier-green)" points="838,372 1072,372 1143,550 770,550"/>

    <!-- peak -->
    <polygon fill="var(--peak-peach-side)" points="869,238 1045,238 1097,328 817,328"/>
    <polygon fill="var(--peak-peach)" points="894,238 1020,238 1052,328 855,328"/>
    <polygon fill="var(--band-orange-side)" points="887,207 1027,207 1045,238 869,238"/>
    <polygon fill="var(--band-orange)" points="908,207 1006,207 1020,238 894,238"/>
    <polygon fill="var(--apex-red-side)" points="957,85 1027,207 887,207"/>
    <polygon fill="var(--apex-red)" points="957,85 1006,207 908,207"/>

    <!-- labels -->
    <text class="tier-label tier-label--lead" x="952" y="486">PROFITABILITY</text>
    <text class="tier-label tier-label--main" x="697" y="494">LEADER</text>
    <text class="tier-label tier-label--main" x="1206" y="494">PARTNER</text>

    <text class="tier-label tier-label--main" x="570" y="701">PEOPLE</text>
    <text class="tier-label tier-label--main" x="833" y="698">INNOVATION</text>
    <text class="tier-label tier-label--main" x="1078" y="679">BUSINESS</text>
    <text class="tier-label tier-label--main" x="1078" y="718">INTELLIGENCE</text>
    <text class="tier-label tier-label--main" x="1336" y="679">STRATEGIC</text>
    <text class="tier-label tier-label--main" x="1336" y="718">ALLIANCES</text>

    <text class="tier-label tier-label--main" x="960" y="897">FIDUCIARY RESPONSIBILITIES</text>
    <text class="tier-caption" x="970" y="941">Accurate Financials / Internal Controls / Brand Protection / Compliance / Ethics / Cost Management</text>
  </svg>

  <div class="slide-number">C50</div>
</div>
</body>
</html>
```